Vimbalo Food Cafeteria and Food Services

I´m a Mexican Company , I dont know if we can built a US web page, but what we are a Cafeteria and Food Services, basically for industry , we produce food at companies for their employes, I have a Brochure to share if you consider. Our logo was made by your team. We need to have a Web page for our potentials custumers find us easy by internet

Target Market(s)

Food for manufacturers /Industry

Industry/Entity Type

Manufacturer

Number of Pages Required

4 page

Font styles to use
Sans Serif

Requirements
Must have
• Great images, Spanish and English options, our mision , vision , our actual customers , (be able to remove it also), our Certifications, our actual packages for services, our 90 days menu, our catering services, Contact page , Cafeteria Services , our meals serve now .
Nice to have
• Great pics, easy to access , and easy to move into the web page, nutricional ideas.
Should not have
• Fluorescent Color , or brilliant

```html
<!DOCTYPE html>
<html lang="en">
<head>
<meta charset="utf-8">
<title>Vimbalo Cafeteria and Food Services</title>
<link href="https://fonts.googleapis.com/css2?family=Montserrat:wght@700;800&family=Raleway:wght@400;500;700;800&family=Roboto+Slab:wght@700&display=swap" rel="stylesheet">
<style>
  :root {
    --green: #33c233;
    --maroon: #4a1212;
    --orange: #e05a14;
    --orange-text: #c9520f;
    --yellow: #fedb33;
    --cater-red: #d9461c;
    --charcoal: #3a3a3a;
    --paper: #f1f1f1;
    --body-text: #5b3030;
    --grey-text: #8a8a8a;
    --white: #ffffff;
  }
  * { margin: 0; padding: 0; box-sizing: border-box; }
  html, body { width: 1200px; height: 946px; overflow: hidden; }
  body {
    position: relative;
    font-family: "Raleway", sans-serif;
    background: linear-gradient(180deg, var(--charcoal) 0, #2f2f2f 446px, #dcdcdc 447px, var(--paper) 560px, var(--paper) 100%);
  }
  .page { position: absolute; left: 150px; top: 42px; width: 900px; height: 589px; background: var(--white); }

  .nav-bar { position: absolute; left: 0; top: 0; width: 900px; height: 53px; background: var(--green); }
  .zigzag {
    position: absolute; left: 0; top: 0; width: 100%; height: 5px;
    background:
      linear-gradient(135deg, var(--white) 50%, transparent 50%) 0 0 / 10px 10px repeat-x,
      linear-gradient(225deg, var(--white) 50%, transparent 50%) 0 0 / 10px 10px repeat-x;
  }
  .logo-panel { position: absolute; left: 27px; top: 0; width: 200px; height: 53px; background: var(--white); }
  .brand { position: absolute; left: 74px; top: 62px; display: flex; align-items: center; gap: 6px; }
  .brand-mark { width: 14px; height: 14px; border-radius: 50%; background: var(--orange); }
  .brand-name { font-family: "Montserrat", sans-serif; font-weight: 800; font-size: 26px; color: var(--maroon); line-height: 1; }
  .brand-tag { position: absolute; left: 76px; top: 92px; font-family: "Montserrat", sans-serif; font-weight: 700; font-size: 7.5px; color: var(--maroon); }

  .main-nav { position: absolute; left: 264px; top: 18px; display: flex; gap: 0; }
  .main-nav a { font-family: "Roboto Slab", serif; font-weight: 700; font-size: 14px; color: var(--white); text-decoration: none; margin-right: 33px; letter-spacing: 0.2px; }
  .social { position: absolute; right: 25px; top: 22px; display: flex; gap: 7px; }
  .social span { width: 9px; height: 9px; border-radius: 50%; background: var(--white); }

  .hero-title { position: absolute; left: 50px; top: 156px; font-family: "Montserrat", sans-serif; font-weight: 800; font-size: 27px; line-height: 27px; color: var(--maroon); width: 420px; }
  .hero-text { position: absolute; left: 50px; top: 264px; width: 480px; font-size: 11px; line-height: 13.5px; color: var(--body-text); }
  .cup-art { position: absolute; left: 54px; top: 340px; width: 64px; height: 71px; border-radius: 8px 8px 30px 30px; background: linear-gradient(160deg, #e36a2a, #a8400f); }
  .schedule-title { position: absolute; left: 128px; top: 340px; font-weight: 700; font-size: 18px; color: var(--orange-text); }
  .schedule { position: absolute; left: 129px; top: 366px; font-size: 11px; line-height: 13.6px; color: var(--orange-text); list-style: none; }
  .schedule b { font-weight: 700; }
  .hero-photo { position: absolute; left: 530px; top: 53px; width: 370px; height: 392px; background: linear-gradient(135deg, #ffffff 0%, #e9c2a5 35%, #f2661f 70%, #e4531a 100%); }

  .book { position: absolute; left: 0; top: 445px; width: 316px; height: 144px; background: var(--orange); color: var(--white); padding: 28px 0 0 42px; }
  .book-label { font-family: "Montserrat", sans-serif; font-weight: 700; font-size: 18px; line-height: 20px; }
  .book-phone { font-family: "Montserrat", sans-serif; font-weight: 700; font-size: 22px; line-height: 24px; }
  .book-address { margin-top: 14px; font-size: 11px; line-height: 13px; font-weight: 700; }
  .cater { position: absolute; left: 316px; top: 445px; width: 584px; height: 144px; background: var(--yellow); }
  .bowl-art { position: absolute; left: 0; top: 14px; width: 122px; height: 122px; border-radius: 50%; background: radial-gradient(circle, #b24a22 0%, #d97d3a 60%, #f0b54c 100%); }
  .cater-title { position: absolute; left: 142px; top: 33px; font-weight: 700; font-size: 21px; color: var(--cater-red); }
  .cater-text { position: absolute; left: 142px; top: 70px; width: 420px; font-size: 11px; line-height: 13px; color: var(--cater-red); }

  .meals-title { position: absolute; left: 0; top: 663px; width: 1200px; text-align: center; font-weight: 800; font-size: 27px; color: var(--maroon); letter-spacing: 0.3px; }
  .meal { position: absolute; top: 725px; width: 290px; height: 112px; }
  .meal-photo { position: absolute; left: 0; top: 0; width: 127px; height: 112px; }
  .meal-name { position: absolute; left: 156px; top: 6px; font-weight: 700; font-size: 14px; color: var(--orange-text); white-space: nowrap; }
  .meal-price { position: absolute; left: 157px; top: 25px; font-weight: 700; font-size: 14px; color: var(--orange-text); }
  .meal-desc { position: absolute; left: 149px; top: 50px; width: 130px; font-size: 9.5px; line-height: 13.5px; color: var(--grey-text); }

  .footer { position: absolute; left: 0; top: 894px; width: 1200px; height: 52px; background: var(--green); color: var(--white); font-size: 9.5px; }
  .footer .zigzag {
    background:
      linear-gradient(135deg, var(--paper) 50%, transparent 50%) 0 0 / 10px 10px repeat-x,
      linear-gradient(225deg, var(--paper) 50%, transparent 50%) 0 0 / 10px 10px repeat-x;
  }
  .copyright { position: absolute; left: 150px; top: 25px; }
  .legal { position: absolute; right: 148px; top: 25px; }
</style>
</head>
<body>
  <div class="page">
    <div class="nav-bar"><div class="zigzag"></div></div>
    <div class="logo-panel"></div>
    <div class="brand"><span class="brand-mark"></span><span class="brand-name">Vimbalo</span></div>
    <div class="brand-tag">Cafeteria and Food Services</div>
    <nav class="main-nav">
      <a href="#">HOME</a><a href="#">ABOUT</a><a href="#">MENU</a><a href="#">PRICE LIST</a><a href="#">CONTACT US</a>
    </nav>
    <div class="social"><span></span><span></span><span></span><span></span></div>

    <h1 class="hero-title">Praesent vestibulum aenean nonummy hendrerit mauris. Hasellus porta.</h1>
    <p class="hero-text">Praesent vestibulum aenean nonummy hendrerit mauris. Hasellus porta. Fusce suscipit varius mi. Cum sociis natoque penatibus magnis dis parturient montes nascetur ridiculus mus. Nulla dui. Fusce feugiat malesuada odio. Morbi nunc odio gravida. at cursus nec luctus a lorem. Maecenas tristique orci ac sem. Duis ultricies pharetra magna. Donec accumsan malesuada orci.</p>
    <div class="cup-art" role="img" aria-label="Illustration of a terracotta coffee cup"></div>
    <h2 class="schedule-title">Cafeteria Schedule</h2>
    <ul class="schedule">
      <li><b>MON - FRI :</b> 7:00 am to 5:00 pm</li>
      <li><b>SATURDAY :</b> 9:00 am to 9:00 pm</li>
      <li><b>SUNDAY :</b> 8:00 am to 7:00 pm</li>
    </ul>
    <div class="hero-photo" role="img" aria-label="Photo of a woman in an orange sweater eating a taco"></div>

    <div class="book">
      <div class="book-label">Book now:</div>
      <div class="book-phone">800 555 0147</div>
      <div class="book-address">Calle Robles 415 Col.<br>Jardines, Valle Norte B. C.<br>e-mail: mail@vimbalo.com</div>
    </div>
    <div class="cater">
      <div class="bowl-art" role="img" aria-label="Illustration of bowls of soup and grilled meat"></div>
      <h2 class="cater-title">CATER YOUR COMPANY WITH US!</h2>
      <p class="cater-text">Maecenas tristique orci ac sem. Duis ultricies pharetra magna. Donec accumsan malesuada orci.um sociis natoque penatibus magnis dis parturient montes nascetur ridiculus mus.</p>
    </div>
  </div>

  <h2 class="meals-title">OUR MEALS SERVE NOW</h2>

  <article class="meal" style="left:155px">
    <div class="meal-photo" role="img" aria-label="Photo of Mexican fajitas wraps" style="background:linear-gradient(135deg,#e8dcc4,#7aa83a 55%,#c8452a)"></div>
    <h3 class="meal-name">MEXICAN FAJITAS</h3>
    <div class="meal-price">$25.50</div>
    <p class="meal-desc">Dusce suscipit varius mi. Cum sociis natoque penatibus magnis dis parturient montes nascetur ridiculus mus ...</p>
  </article>
  <article class="meal" style="left:455px">
    <div class="meal-photo" role="img" aria-label="Photo of a plate of chili con carne" style="background:linear-gradient(160deg,#1c1c1c,#3a2a22 50%,#b8432a 80%,#ddd)"></div>
    <h3 class="meal-name">CHILI CON CARNE</h3>
    <div class="meal-price">$25.50</div>
    <p class="meal-desc">Dusce suscipit varius mi. Cum sociis natoque penatibus magnis dis parturient montes nascetur ridiculus mus ...</p>
  </article>
  <article class="meal" style="left:755px">
    <div class="meal-photo" role="img" aria-label="Photo of a bowl of Mexican chili with beans" style="background:linear-gradient(150deg,#d9a24a,#a3401c 50%,#5a1f12)"></div>
    <h3 class="meal-name">MEXICAN CON CHILI</h3>
    <div class="meal-price">$25.50</div>
    <p class="meal-desc">Dusce suscipit varius mi. Cum sociis natoque penatibus magnis dis parturient montes nascetur ridiculus mus ...</p>
  </article>

  <footer class="footer">
    <div class="zigzag"></div>
    <div class="copyright">© Copyright Vimbalo Cafeteria and Food Services. All Rights Reserved</div>
    <div class="legal">Terms &nbsp;|&nbsp; Privacy Policy</div>
  </footer>
</body>
</html>
```